Letterhead Design

We are a physical security and protective intelligence firm based in regional NSW, Australia. We are in need of a professionally designed letter head/ document for our company Valtrix Security. Ref. www.valtrixsecurity.com.au for detailed company information. MUST include Master Licence and ABN details.

Target Market(s)

corporate business, celebrities, property managers, entertainment professionals

Industry/Entity Type

Security

Requirements
Must have
• Must look sharp, professional and cutting edge. Think 419, Silent Directorate, QX3/4 and NOT the movie known as "Dwayne Tuffle Lot Patrol". :-)
Should not have
• Please NO cheesy security guards standing around in uniform. Think protective intelligence and counter terrorism operations. We do not wish to convey an image of a guard company, we offer this service but it is not what we aim to promote. Seek to achieve a higher level approach... elite as opposed to "the usual" guard services etc.

```html
<!DOCTYPE html>
<html lang="en">
<head>
<meta charset="utf-8">
<title>Valtrix Security Letterhead</title>
<link href="https://fonts.googleapis.com/css2?family=Source+Sans+3:wght@400;600&display=swap" rel="stylesheet">
<style>
  :root {
    --backdrop: #59595b;
    --paper: #ffffff;
    --header-dark: #0d0d0f;
    --brand-silver: #d2d4d8;
    --tagline: #e8e8e8;
    --ink: #111111;
    --body-text: #7a7a7c;
    --rule: #1a1a1a;
  }
  * { margin: 0; padding: 0; box-sizing: border-box; }
  html, body { width: 1200px; height: 999px; overflow: hidden; }
  body {
    background: var(--backdrop);
    font-family: "Source Sans 3", "Myriad Pro", sans-serif;
    position: relative;
  }
  .letterhead {
    position: absolute;
    left: 300px; top: 77px;
    width: 600px; height: 844px;
    background: var(--paper);
    overflow: hidden;
  }
  .header-band { position: absolute; left: 0; top: 0; }
  .brand {
    position: absolute;
    left: 0; top: 61px;
    width: 322px;
    text-align: center;
  }
  .brand-name {
    color: var(--brand-silver);
    font-size: 28px;
    font-weight: 600;
    letter-spacing: 0.6px;
    text-transform: uppercase;
    line-height: 32px;
  }
  .brand-tagline {
    margin-top: 5px;
    color: var(--tagline);
    font-size: 11px;
    font-weight: 400;
    line-height: 12px;
  }
  .contact {
    position: absolute;
    right: 14px; top: 29px;
    text-align: right;
    color: var(--ink);
    font-size: 10.4px;
    line-height: 13px;
  }
  .contact .licensing { margin-bottom: 9px; }
  .header-rule {
    position: absolute;
    left: 0; top: 129px;
    width: 600px; height: 3px;
    background: var(--rule);
  }
  .watermark-area {
    position: absolute;
    left: 220px; top: 500px;
    width: 400px; height: 360px;
    background: radial-gradient(ellipse at 85% 70%, rgba(220,222,228,0.55), rgba(240,241,244,0.25) 55%, rgba(255,255,255,0) 75%);
  }
  .letter-body {
    position: absolute;
    left: 44px; top: 236px;
    width: 512px;
    color: var(--body-text);
    font-size: 11.6px;
    line-height: 14.3px;
    text-align: justify;
  }
  .letter-body p + p { margin-top: 14.3px; }
</style>
</head>
<body>
  <div class="letterhead">
    <svg class="header-band" width="600" height="130" viewBox="0 0 600 130" aria-hidden="true">
      <polygon points="0,0 437,0 333,126 0,126" fill="var(--header-dark)"/>
    </svg>

    <div class="brand">
      <div class="brand-name">Valtrix Security</div>
      <div class="brand-tagline">Precision in Protective Intelligence</div>
    </div>

    <div class="contact">
      <div class="licensing">
        Master Licence: 52817 3046<br>
        ABN:&nbsp;&nbsp;&nbsp;&nbsp;&nbsp;&nbsp;&nbsp;&nbsp;&nbsp;&nbsp;&nbsp;61 308 492 117<br>
        SPIA Member: 00 07 31 58
      </div>
      <div class="details">
        T :&nbsp; (02) 5550 4182 or 0400 555 219<br>
        E :&nbsp;&nbsp;&nbsp;&nbsp;&nbsp;&nbsp; office@ValtrixSecurity.com.au<br>
        A:&nbsp; Kelmore, New South Wales, Australia, 2351
      </div>
    </div>

    <div class="header-rule"></div>

    <div class="watermark-area" role="img" aria-label="Faint decorative watermark of soft grey sweeping stripes and stars"></div>

    <div class="letter-body">
      <p>Lorem ipsum dolor sit amet, consectetur adipiscing elit. Integer facilisis vulputate augue, dapibus ultricies velit egestas vel. Duis ligula arcu, condimentum eu vehicula in, consequat eget odio. Ut egestas, leo ut fringilla convallis, nisl dolor consectetur erat, pretium porttitor justo nulla a tortor. Duis vel eleifend felis. Praesent at massa porta, dapibus est non, placerat eros. Vestibulum ultrices nisi et leo mollis, sed fermentum enim tincidunt. Vestibulum a condimentum tortor. Curabitur nec euismod purus, id ornare magna. Nulla lorem ante, volutpat vitae tempor sit amet, convallis et lectus. Curabitur porta faucibus massa quis egestas. Etiam vel aliquam lacus. Morbi pellentesque volutpat ante, at vestibulum risus consequat rhoncus. Vestibulum ante ipsum primis in faucibus orci luctus et ultrices posuere cubilia Curae; Nunc ac tincidunt nibh. Sed commodo, turpis sed rhoncus euismod, libero odio molestie quam, at blandit leo massa ut ligula. Vivamus tristique velit augue, eget aliquet nulla facilisis non.</p>
      <p>Curabitur facilisis, risus ut malesuada ornare, nunc diam sollicitudin elit, id ornare quam mauris ac dolor. Nulla et nulla interdum leo eleifend eleifend non consequat felis. Suspendisse cursus semper eros nec ullamcorper. Nam scelerisque adipiscing metus, nec mattis dui molestie a. Proin convallis at nulla eu laoreet. In eleifend blandit massa vitae tincidunt. Suspendisse rutrum augue eu mauris tincidunt auctor vitae in lectus. Donec tincidunt ligula vulputate, tincidunt erat a, sollicitudin tellus. Pellentesque dictum, justo vitae mollis lobortis, orci metus euismod urna, eget ultrices quam purus ut tortor.</p>
      <p>Nam mollis libero et aliquam fermentum. Suspendisse potenti. Fusce adipiscing nibh et lobortis scelerisque. Ut ut erat odio. Aenean semper dolor sed justo semper venenatis. Vestibulum dapibus, massa eget euismod condimentum, mauris mi porttitor magna, in mollis augue eros in sem. Ut tristique, quam eget ultrices rhoncus, ipsum nunc lobortis orci, in gravida purus velit at orci. Sed pellentesque mauris ut lacus gravida sodales. Sed cursus felis vitae tellus tempus, vitae eleifend augue pulvinar. In imperdiet pretium nunc, vitae congue justo sodales sit amet. Etiam gravida mi mauris, et mollis leo congue id. Mauris congue a lacus eget cursus.</p>
      <p>Suspendisse bibendum varius lectus a dignissim. Cras accumsan felis vitae ultrices congue. Aliquam erat volutpat. Maecenas ut felis enim. Proin suscipit gravida odio at faucibus. Vivamus euismod mauris ut magna pulvinar, quis aliquet elit viverra. Interdum et malesuada fames ac ante ipsum primis in faucibus. Fusce eget risus dignissim, egestas sem sed, vulputate odio. Maecenas luctus eleifend eros, sed vehicula lacus tempus id. Nulla adipiscing mollis metus, eget tincidunt risus feugiat nec. Vestibulum in viverra massa, ac luctus est. Nullam bibendum consectetur eleifend.</p>
    </div>
  </div>
</body>
</html>
```